Powepoint Templates From Logo

Hello,

I am looking for a template for PowerPoint presentations for a new company selling LED's. The PowerPoint should keep the look and feel of our newly designed website ( which is still under development ) http://brivonlux.com/development/

I have attached our Logo which should be included in this template.
This PowerPoint will be used towards client during demonstrations and for internal use.

This template should be complete with fonts and colors of the text for both headlines and bullets/normal text.

I guess the easiest way for me to determine what I like is to see some dummy info/text on the submitted designs.

Thanks

Industry/Entity Type

It Company

Requirements
Must have
• Should include our logo

```html
<!DOCTYPE html>
<html lang="en">
<head>
<meta charset="UTF-8">
<title>Advantages of LEDs – Title &amp; Content Slide</title>
<link rel="stylesheet" href="https://fonts.googleapis.com/css2?family=Varela+Round&family=Carlito&display=swap">
<style>
  :root {
    --bg: #ffffff;
    --title-green: #3ed120;
    --text-dark: #1a1a1a;
    --grass-light: #e6f3cf;
    --grass-mid: #a9d86a;
    --grass-deep: #7cc242;
    --brand-grey: #8a8a8a;
    --brand-green: #8cc63f;
  }
  html, body {
    margin: 0;
    padding: 0;
    overflow: hidden;
    background: var(--bg);
  }
  .canvas {
    position: relative;
    width: 1200px;
    height: 900px;
    background: var(--bg);
    overflow: hidden;
  }
  .slide-title {
    position: absolute;
    left: 116px;
    top: 82px;
    margin: 0;
    font-family: "Varela Round", sans-serif;
    font-weight: 400;
    font-size: 54px;
    letter-spacing: -1px;
    color: var(--title-green);
  }
  .bullet-list {
    position: absolute;
    left: 120px;
    top: 196px;
    margin: 0;
    padding: 0;
    list-style: none;
    font-family: "Carlito", sans-serif;
    font-size: 42px;
    color: var(--text-dark);
  }
  .bullet-list li {
    height: 70px;
    line-height: 52px;
    display: flex;
    align-items: flex-start;
  }
  .bullet-list li::before {
    content: "\2756";
    width: 52px;
    font-size: 30px;
    flex: none;
  }
  .grass-band {
    position: absolute;
    left: 50px;
    top: 665px;
    width: 1095px;
    height: 168px;
  }
  .brand-mark {
    position: absolute;
    left: 910px;
    top: 740px;
    display: flex;
    align-items: center;
    gap: 12px;
  }
  .brand-dot {
    width: 56px;
    height: 56px;
    border-radius: 50%;
    background: var(--brand-green);
  }
  .brand-name {
    font-family: "Varela Round", sans-serif;
    font-size: 36px;
    color: var(--brand-grey);
  }
  .layout-caption {
    position: absolute;
    left: 0;
    width: 100%;
    top: 846px;
    margin: 0;
    text-align: center;
    font-family: "Varela Round", sans-serif;
    font-weight: 700;
    font-size: 34px;
    letter-spacing: -1px;
    color: #000;
    -webkit-text-stroke: 0.8px #000;
  }
</style>
</head>
<body>
<div class="canvas">
  <h1 class="slide-title">Advantages of LEDs</h1>
  <ul class="bullet-list">
    <li>Environmentally friendly</li>
    <li>Up to 80% more efficient</li>
    <li>Longer operational life</li>
    <li>More cost effective</li>
  </ul>

  <svg class="grass-band" viewBox="0 0 1095 168" role="img" aria-label="Illustration of green grass growing along a gentle rolling hill">
    <defs>
      <linearGradient id="hillFill" x1="0" y1="0" x2="1" y2="0">
        <stop offset="0" stop-color="var(--grass-deep)"/>
        <stop offset="0.55" stop-color="var(--grass-mid)"/>
        <stop offset="1" stop-color="var(--grass-light)"/>
      </linearGradient>
      <linearGradient id="grassFade" x1="0" y1="0" x2="1" y2="0">
        <stop offset="0" stop-color="var(--grass-mid)" stop-opacity="0.7"/>
        <stop offset="1" stop-color="var(--grass-light)" stop-opacity="0.5"/>
      </linearGradient>
    </defs>
    <path d="M0 20 C120 40 300 120 520 120 C720 120 900 50 1095 20 L1095 168 L0 168 Z" fill="url(#grassFade)"/>
    <path d="M0 50 C140 70 320 130 520 130 C720 130 900 70 1095 40 L1095 168 L0 168 Z" fill="url(#hillFill)"/>
  </svg>

  <div class="brand-mark">
    <span class="brand-dot"></span>
    <span class="brand-name">Brivonlux</span>
  </div>

  <p class="layout-caption">Title &amp; Content Slide</p>
</div>
</body>
</html>
```